Fatigued and Overloaded by COVID Messages? We need original illustrations to show that.

Everywhere you look there are messages about COVID. That is leading many people to feel fatigued and overloaded by the messages.

We surveyed U.S. adults March 20th - 24th, 2020 and measured message fatigue, information overload, perceived repetition, and perceived exaggeration. Here is how participants responded:

When it comes to coronavirus . . .
55% feel exhausted by all the messages.
54% feel overloaded by the amount of information.
51% feel that the messages are repetitive.
47% feel like messages exaggerate how bad it is.

In other words, almost half of U.S. adults show signs of message fatigue, information overload, perceived message repetition, and perceived message exaggeration.

We will continue to survey 400 adults every week for the next 16 weeks. Each time we will measure message fatigue, information overload, perceived repetition, and perceived exaggeration. We expect that it will increase over time.

What are we looking for? We need innovative and original illustrations that attempt to communicate these findings. The illustrations would visualize message fatigue, information overload, perceived message repetition, and perceived message exaggeration.

What sort of visual are we looking for? Our preference is for an original illustration (or set of illustrations). Our preference is for creative and powerful illustrations, but we are also open to the creative and well-executed infographics.

We need these images fast . We will award monetary prizes to the 3 best designs. If we like more than that, then we might purchase more (e.g., in past contests, we have purchased as many as 30 designs).

What we will need:
(1) The illustrations must be original and we will need the photoshop and/or illustrator files for all artwork. (By original, we mean that the illustrations are 100% created by you. Our organization requires that we utilize only original illustrated work. We have had issues with free imagery being pirated and reposted as free. We sidestep that issue by just having everything created.)

(2) The illustration should say, somewhere: "Based on a survey of 400 U.S. adults conducted March 20 - 24th, 2020."

(3) We will have almost 4 months worth of data by the time this is done. In other words, the illustrations might be able to help us present that weekly data.

(4) We have conducted other Artvendo projects. It might be helpful to examine designs we liked in the past. For example, here is another COVID project we just finished:

https://jobs.artvendo-example.com/job/5162048

Target Market(s)

U.S. adults

Requirements
Must have
• Original illustrations. Mobile friendly design. People will view this on their smartphones.
Nice to have
• A design that we can use to communicate the data across time.

```html
<!DOCTYPE html>
<html lang="en">
<head>
<meta charset="utf-8">
<title>Fatigued and Overloaded by COVID Messages?</title>
<link href="https://fonts.googleapis.com/css2?family=Bebas+Neue&family=Roboto+Condensed:ital,wght@1,500;1,700&family=Montserrat:ital,wght@0,800;1,700;1,800&display=swap" rel="stylesheet">
<style>
  :root{
    --yellow:#fdee00;
    --yellow-soft:#f7e93a;
    --navy:#0b137a;
    --ink:#000;
    --red:#ff0d0d;
    --orange:#ff5a0c;
    --bar-fill:#2681b8;
    --virus-mauve:#c09194;
    --virus-pink:#d2adad;
    --virus-beige:#e6d6c2;
    --figure-hair:#9b3a0c;
    --figure-skin:#e3b68c;
    --figure-shirt:#2c3590;
    --figure-stripe:#19e6f0;
    --paper:#fff;
  }
  *{margin:0;padding:0;box-sizing:border-box}
  html,body{width:675px;height:1200px;overflow:hidden;background:var(--paper)}
  .infographic{position:relative;width:675px;height:1200px;overflow:hidden;background:var(--paper)}
  .abs{position:absolute}

  .source-line{left:0;top:10px;width:675px;text-align:center;font-family:"Roboto Condensed",sans-serif;font-style:italic;font-weight:500;font-size:19px;color:var(--ink);white-space:nowrap}
  .source-line strong{color:var(--navy);font-size:23px;font-weight:500}

  .decor-virus-top{left:505px;top:0;width:170px;height:295px;background:radial-gradient(ellipse at 75% 30%,var(--virus-pink) 0 55%,rgba(210,173,173,0) 72%)}
  .decor-virus-bottom{left:145px;top:805px;width:245px;height:285px;background:radial-gradient(ellipse at 50% 50%,var(--virus-beige) 0 58%,rgba(230,214,194,0) 72%)}
  .decor-blob-bottom{left:0;top:1048px;width:373px;height:152px;background:linear-gradient(90deg,var(--virus-mauve) 0 85%,rgba(192,145,148,.6) 100%);border-radius:0 60px 0 0}

  .title-band{left:0;top:44px;width:675px;height:147px;background:var(--yellow)}
  .title{position:absolute;left:0;width:675px;text-align:center;font-family:"Bebas Neue",sans-serif;line-height:1;color:var(--ink);white-space:nowrap}
  .title-line1{top:11px;font-size:62px;letter-spacing:1.2px}
  .title-line2{top:70px;font-size:68px;letter-spacing:1px}
  .title-line2 .accent{color:var(--navy);font-size:74px}

  .figure{border-radius:38px 38px 10px 10px;background:linear-gradient(180deg,var(--figure-hair) 0 10%,var(--figure-skin) 24% 52%,var(--figure-shirt) 64% 100%);opacity:.92}
  .stat-value{font-family:"Montserrat",sans-serif;font-weight:800;font-size:35px;line-height:1;color:var(--red)}
  .stat-label{font-family:"Roboto Condensed",sans-serif;font-style:italic;font-weight:700;font-size:11.5px;line-height:13.5px;color:var(--ink);white-space:nowrap}
  .bar{border:3px solid var(--ink);border-radius:6px;background:var(--paper);overflow:hidden}
  .bar-fill{height:100%;background:var(--bar-fill)}

  .meaning-box{left:0;top:864px;width:447px;height:184px;background:var(--yellow-soft);opacity:.97}
  .meaning-title{position:absolute;left:35px;top:21px;font-family:"Bebas Neue",sans-serif;font-size:43px;line-height:1;color:var(--orange);white-space:nowrap;letter-spacing:.3px}
  .meaning-text{position:absolute;left:34px;top:69px;width:410px;font-family:"Montserrat",sans-serif;font-style:italic;font-weight:700;font-size:18.6px;line-height:23.5px;color:var(--ink)}
  .meaning-text b{font-weight:800}

  .figure-large{left:429px;top:830px;width:246px;height:370px;border-radius:110px 110px 0 0;background:linear-gradient(180deg,var(--figure-hair) 0 8%,var(--figure-skin) 20% 52%,var(--figure-shirt) 66% 100%)}
</style>
</head>
<body>
<main class="infographic">
  <div class="abs decor-virus-top" role="img" aria-label="Decorative virus particle shape"></div>
  <div class="abs decor-virus-bottom" role="img" aria-label="Decorative virus particle shape"></div>
  <div class="abs decor-blob-bottom" role="img" aria-label="Decorative virus particle shape"></div>

  <p class="abs source-line">Based on a survey of <strong>400 U.S. adults</strong> conducted March 20 - 24th, 2020</p>

  <header class="abs title-band">
    <h1>
      <span class="title title-line1">FATIGUED AND OVERLOADED</span>
      <span class="title title-line2">BY <span class="accent">COVID MESSAGES?</span></span>
    </h1>
  </header>

  <section class="stats">
    <div class="abs figure" style="left:78px;top:210px;width:84px;height:130px" role="img" aria-label="Illustrated man looking exhausted at his buzzing phone"></div>
    <p class="abs stat-value" style="left:174px;top:228px">55%</p>
    <p class="abs stat-label" style="left:175px;top:260px">feel exhausted by all the messages.</p>
    <div class="abs bar" style="left:146px;top:282px;width:427px;height:49px"><div class="bar-fill" style="width:58%"></div></div>

    <div class="abs figure" style="left:78px;top:375px;width:80px;height:130px" role="img" aria-label="Illustrated man frowning and cursing at his phone"></div>
    <p class="abs stat-value" style="left:175px;top:384px">54%</p>
    <p class="abs stat-label" style="left:175px;top:415px">feel overloaded by the amount<br>of information.</p>
    <div class="abs bar" style="left:147px;top:446px;width:429px;height:49px"><div class="bar-fill" style="width:53%"></div></div>

    <div class="abs figure" style="left:75px;top:530px;width:80px;height:130px" role="img" aria-label="Illustrated man looking bored at his buzzing phone"></div>
    <p class="abs stat-value" style="left:171px;top:548px">51%</p>
    <p class="abs stat-label" style="left:171px;top:578px">feel that the messages are repetitive.</p>
    <div class="abs bar" style="left:142px;top:600px;width:434px;height:49px"><div class="bar-fill" style="width:48%"></div></div>

    <div class="abs figure" style="left:75px;top:683px;width:80px;height:132px" role="img" aria-label="Illustrated man looking shocked at his phone"></div>
    <p class="abs stat-value" style="left:172px;top:693px">47%</p>
    <p class="abs stat-label" style="left:172px;top:724px">feel like messages exaggerate<br>how bad it is.</p>
    <div class="abs bar" style="left:140px;top:756px;width:436px;height:48px"><div class="bar-fill" style="width:45%"></div></div>
  </section>

  <div class="abs figure-large" role="img" aria-label="Illustrated frustrated man holding a phone surrounded by COVID-19 notifications"></div>

  <section class="abs meaning-box">
    <h2 class="meaning-title">WHAT DOES THIS DATA MEAN?</h2>
    <p class="meaning-text"><b>Almost half of U.S. adults</b> show signs of message fatigue, information overload, perceived message repetition, and perceived message exaggeration.</p>
  </section>
</main>
</body>
</html>
```